VelaCure Wellness Business Cards

I am looking to have luxury business cards made for my IV Therapy and Wellness business.
Updates

Target Market(s)

Health and Wellness professionals

Industry/Entity Type

MedSpa

Contact Information for Business Card

Tobin Haverly, MSN, RN, CCRN Tobin@velacurewellness.com (916) 582-3179 QR code to website www.velacurewellness.com

```html
<!DOCTYPE html>
<html lang="en">
<head>
<meta charset="UTF-8">
<title>VelaCure Wellness Business Cards</title>
<link rel="stylesheet" href="https://fonts.googleapis.com/css2?family=Poppins:wght@400;500;600;700&family=Roboto:wght@400;500&display=swap">
<style>
  :root {
    --backdrop: #161617;
    --card: #2a2a2b;
    --card-edge: #323233;
    --emboss: #4b4b4d;
    --emboss-light: #5a5a5c;
    --white: #ffffff;
    --accent: #1ea1e6;
  }
  * { margin: 0; padding: 0; box-sizing: border-box; }
  html, body {
    width: 1200px; height: 840px; overflow: hidden;
    background: var(--backdrop);
  }
  .canvas { position: relative; width: 1200px; height: 840px; }

  .card {
    position: absolute;
    width: 560px; height: 320px;
    background: var(--card);
    border-radius: 22px;
    border: 1px solid var(--card-edge);
  }

  /* Logo side */
  .card--brand { left: 70px; top: 90px; }
  .brand-mark {
    position: absolute; left: 0; right: 0; top: 50%;
    transform: translateY(-50%);
    display: flex; flex-direction: column; align-items: center; gap: 10px;
  }
  .brand-mark__dot {
    width: 34px; height: 34px; border-radius: 50%;
    border: 2px solid var(--emboss-light);
  }
  .brand-mark__name {
    font-family: "Poppins", sans-serif;
    font-weight: 400; font-size: 44px; letter-spacing: 1px;
    color: var(--emboss);
  }
  .brand-mark__rule {
    width: 260px; height: 2px; background: var(--emboss);
  }

  /* Contact side */
  .card--contact { left: 570px; top: 440px; }
  .contact-logo {
    position: absolute; left: 0; right: 0; top: 62px;
    display: flex; justify-content: center; align-items: center; gap: 12px;
  }
  .contact-logo__dot {
    width: 22px; height: 22px; border-radius: 50%; background: var(--accent);
  }
  .contact-logo__name {
    font-family: "Poppins", sans-serif;
    font-weight: 700; font-size: 40px; letter-spacing: -0.5px;
    color: var(--white);
  }
  .contact-details {
    position: absolute; left: 28px; right: 24px; bottom: 58px;
    display: flex; align-items: center; justify-content: center; gap: 20px;
  }
  .person { text-align: right; flex: 0 0 auto; }
  .person__name {
    font-family: "Poppins", sans-serif;
    font-weight: 600; font-size: 21px; color: var(--accent);
    letter-spacing: 0.3px; line-height: 1.1;
  }
  .person__title {
    font-family: "Poppins", sans-serif;
    font-weight: 400; font-size: 15px; color: var(--white);
  }
  .divider { width: 1px; height: 72px; background: var(--white); opacity: .8; flex: 0 0 auto; }
  .contact-list { list-style: none; display: flex; flex-direction: column; gap: 5px; }
  .contact-list__item {
    display: flex; align-items: center; gap: 7px;
    font-family: "Roboto", sans-serif; font-size: 15px; color: var(--white);
    white-space: nowrap;
  }
  .contact-icon { width: 17px; height: 17px; flex: 0 0 auto; }
</style>
</head>
<body>
<main class="canvas">

  <section class="card card--brand" aria-label="Business card, logo side">
    <div class="brand-mark">
      <span class="brand-mark__dot"></span>
      <span class="brand-mark__name">VelaCure Wellness</span>
      <span class="brand-mark__rule"></span>
    </div>
  </section>

  <section class="card card--contact" aria-label="Business card, contact side">
    <div class="contact-logo">
      <span class="contact-logo__dot"></span>
      <span class="contact-logo__name">VelaCure Wellness</span>
    </div>

    <div class="contact-details">
      <div class="person">
        <p class="person__name">TOBIN HAVERLY</p>
        <p class="person__title">MSN, RN, CCRN</p>
      </div>
      <span class="divider"></span>
      <ul class="contact-list">
        <li class="contact-list__item">
          <svg class="contact-icon" viewBox="0 0 20 20" aria-hidden="true">
            <circle cx="10" cy="10" r="10" fill="var(--accent)"/>
            <path d="M6.5 5.5l2 0 1 2.5-1.2 1a6 6 0 0 0 2.7 2.7l1-1.2 2.5 1v2a1 1 0 0 1-1 1A8 8 0 0 1 5.5 6.5a1 1 0 0 1 1-1z" fill="#fff"/>
          </svg>
          (916) 582-3179
        </li>
        <li class="contact-list__item">
          <svg class="contact-icon" viewBox="0 0 20 20" aria-hidden="true">
            <circle cx="10" cy="10" r="10" fill="var(--accent)"/>
            <rect x="5" y="6.5" width="10" height="7" rx="1" fill="#fff"/>
            <path d="M5.5 7l4.5 3.5L14.5 7" stroke="var(--accent)" stroke-width="1.2" fill="none"/>
          </svg>
          Tobin@velacurewellness.com
        </li>
        <li class="contact-list__item">
          <svg class="contact-icon" viewBox="0 0 20 20" aria-hidden="true">
            <circle cx="10" cy="10" r="10" fill="var(--accent)"/>
            <circle cx="10" cy="10" r="5" fill="none" stroke="#fff" stroke-width="1.3"/>
            <path d="M5 10h10M10 5c-2.5 3-2.5 7 0 10M10 5c2.5 3 2.5 7 0 10" fill="none" stroke="#fff" stroke-width="1"/>
          </svg>
          www.velacurewellness.com
        </li>
      </ul>
    </div>
  </section>

</main>
</body>
</html>
```